■依頼の目的/概要
ハルカゼのlumoraで電子書籍出版をします。

■本の内容
40代女性で話すことや伝えること
自分に自信はないけれど

起業したい、
夢や目標を叶えたい、
という方がターゲットです。

声と潜在意識(心)の力を使う「ひだまりトーン」で
人前で自信をもって伝えられるようになったり
やりたいことがどんどん実現できるようになる方法を
書きました。

声や潜在意識を使ったトレーニング、
実例を用いてお伝えしています。

■デザイン要望
40代女性が好むデザインが希望です。
顔写真も入れていただけたらと思います。
その際、手に持っている音符などは載せないようお願いいたします。

お写真と、電子書籍の文章をお送りいたします。

ご応募、心よりお待ちしております!!!

その他何かご不明な点がございましたら、お気軽にご質問下さい。
よろしくお願いいたします。
タイトルは
響きの名手がひもとく
輝く毎日をつくる心の整え方・磨き方
~ひだまりトーンの秘密~

著者は
ひだまりトーンコンサルタント
さとうれな

どうぞよろしくお願いいたします。
LQS表記では、表紙画像のサイズは 50 MB 未満表紙フ
ァイルの理想的な寸法は 2,560 x 1,600 ピクセルとなっています。

文字が見やすいこと。
女性的な優しいイメージと内容が合うもの、
という視点で選ばせていただきました。

素晴らしい作品ばかりで
選ばせていただくのに時間がかかりました。

短期間にも関わらず
素敵な作品を沢山ご応募いただき
どうもありがとうございました!

心より感謝いたします。

機会がございましたら
またどうぞよろしくお願いいたします。

```html
<!DOCTYPE html>
<html lang="ja">
<head>
<meta charset="utf-8">
<title>響きの名手がひもとく 輝く毎日をつくる心の整え方・磨き方</title>
<link rel="stylesheet" href="https://fonts.googleapis.com/css2?family=Noto+Serif+JP:wght@600;800&family=Noto+Sans+JP:wght@500;700&display=swap">
<style>
  :root {
    --paper: #ffffff;
    --ink: #1a1a1a;
    --title-red: #d3242c;
    --band: #111111;
    --band-text: #ffffff;
    --pink-top: #f5cdd8;
    --pink-bottom: #fcebf0;
    --sketch-light: #f1ede8;
    --sketch-dark: #3a3434;
    --portrait-a: #f3d9df;
    --portrait-b: #d9a9b4;
  }
  * { margin: 0; padding: 0; box-sizing: border-box; }
  html, body { width: 814px; height: 1200px; overflow: hidden; background: var(--paper); }
  .cover {
    position: relative;
    width: 814px;
    height: 1200px;
    background: var(--paper);
    overflow: hidden;
    font-family: "Noto Sans JP", sans-serif;
    color: var(--ink);
  }
  .fashion-sketch {
    position: absolute;
    left: 0; top: 0;
    width: 300px; height: 640px;
  }
  .pink-field {
    position: absolute;
    left: 0; top: 700px;
    width: 814px; height: 500px;
    background: linear-gradient(180deg, var(--pink-top) 0%, var(--pink-bottom) 35%, var(--pink-bottom) 100%);
  }
  .title-lead {
    position: absolute;
    left: 250px; top: 14px;
    font-family: "Noto Serif JP", serif;
    font-weight: 800;
    color: var(--title-red);
    font-size: 104px;
    line-height: 1.15;
    letter-spacing: 2px;
    white-space: nowrap;
  }
  .title-lead-tail {
    position: absolute;
    left: 380px; top: 136px;
    font-family: "Noto Serif JP", serif;
    font-weight: 800;
    color: var(--ink);
    font-size: 74px;
    line-height: 1.2;
    letter-spacing: 2px;
    white-space: nowrap;
  }
  .subtitle-band {
    position: absolute;
    left: 330px; top: 262px;
    width: 484px; height: 150px;
    background: var(--band);
    color: var(--band-text);
    font-family: "Noto Serif JP", serif;
    font-weight: 600;
    font-size: 46px;
    line-height: 64px;
    padding: 11px 0 0 20px;
    letter-spacing: 0;
    white-space: nowrap;
  }
  .author {
    position: absolute;
    left: 200px; top: 436px;
    display: flex;
    flex-direction: row-reverse;
    align-items: flex-start;
    gap: 10px;
  }
  .author span {
    writing-mode: vertical-rl;
    font-family: "Noto Serif JP", serif;
    white-space: nowrap;
  }
  .author-role { font-size: 17px; font-weight: 600; }
  .author-label { font-size: 28px; font-weight: 600; padding-top: 92px; }
  .author-name { font-size: 46px; font-weight: 800; letter-spacing: 3px; padding-top: 8px; }
  .portrait {
    position: absolute;
    left: 546px; top: 470px;
    width: 228px; height: 228px;
  }
  .pain-points {
    position: absolute;
    left: 106px; top: 720px;
    list-style: none;
    font-weight: 700;
    font-size: 40px;
    line-height: 50px;
    white-space: nowrap;
  }
  .book-tagline {
    position: absolute;
    left: 90px; top: 872px;
    font-family: "Noto Serif JP", serif;
    font-weight: 800;
    font-size: 50px;
    letter-spacing: 1px;
    white-space: nowrap;
  }
</style>
</head>
<body>
<div class="cover">
  <svg class="fashion-sketch" viewBox="0 0 300 640" role="img" aria-label="ファッションイラスト：白いドレスの女性の後ろ姿">
    <defs>
      <linearGradient id="sketchTone" x1="0" y1="0" x2="1" y2="1">
        <stop offset="0" stop-color="#f1ede8"/>
        <stop offset="0.6" stop-color="#d9d2cc"/>
        <stop offset="1" stop-color="#3a3434"/>
      </linearGradient>
    </defs>
    <rect width="300" height="640" fill="url(#sketchTone)"/>
  </svg>

  <div class="pink-field"></div>

  <h1 class="title-lead">響きの名手</h1>
  <div class="title-lead-tail">がひもとく</div>

  <h2 class="subtitle-band">輝く毎日をつくる<br>心の整え方・磨き方</h2>

  <div class="author">
    <span class="author-role">ひだまりトーンコンサルタント</span>
    <span class="author-label">著者</span>
    <span class="author-name">さとうれな</span>
  </div>

  <svg class="portrait" viewBox="0 0 228 228" role="img" aria-label="著者の顔写真">
    <defs>
      <radialGradient id="portraitTone" cx="0.5" cy="0.4" r="0.6">
        <stop offset="0" stop-color="#f3d9df"/>
        <stop offset="1" stop-color="#d9a9b4"/>
      </radialGradient>
    </defs>
    <circle cx="114" cy="114" r="112" fill="url(#portraitTone)"/>
  </svg>

  <ul class="pain-points">
    <li>人前で話すのが苦手</li>
    <li>緊張体質、あがり症</li>
    <li>人見知り、口下手、会話下手</li>
  </ul>
  <p class="book-tagline">～ひだまりトーンの秘密～</p>
</div>
</body>
</html>
```